VENTURE CAPITAL GROUP BUSINESS CARD DESIGN

Venture Capital Group based in SF looking for a bold business card design. No trendy colour explosion, 3D effects etc. Just "simple" optical effects. Works on your brain, keeps your eye focused and sticks to your mind.
Target Market(s)
Technology startups
Industry/Entity Type
Venture Capital
Contact Information for Business Card
BARNABY WHITLOCK
MANAGING PARTNER
817 FERN ST SAN FRANCISCO, CA 94111
415.555.0143 O
415.555.0167 F
415.555.0192 C
barn@halcyonridgefund.example

```html
<!DOCTYPE html>
<html lang="en">
<head>
<meta charset="utf-8">
<title>Halcyon Ridge Fund — Business Card</title>
<link rel="stylesheet" href="https://fonts.googleapis.com/css2?family=Libre+Baskerville:wght@400;700&display=swap">
<style>
  :root {
    --backdrop: #1c1c1c;
    --card: #f7f7f5;
    --card-edge: #e4e4e2;
    --green: #1a8a3c;
    --green-deep: #0f6b2c;
    --ink: #333333;
    --muted: #7a7a7a;
    --facet-light: #fbfbfb;
    --facet-mid: #dcdcdc;
    --facet-dark: #c4c4c4;
  }
  * { box-sizing: border-box; margin: 0; padding: 0; }
  html, body { width: 1200px; height: 873px; overflow: hidden; }
  body {
    background: var(--backdrop);
    font-family: "Libre Baskerville", Georgia, serif;
    color: var(--ink);
    position: relative;
  }
  .card {
    position: absolute;
    width: 540px;
    height: 309px;
    background: var(--card);
    border: 1px solid var(--card-edge);
    box-shadow: 0 12px 30px rgba(0,0,0,.55);
    overflow: hidden;
  }
  .card--front { left: 70px; top: 90px; }
  .card--back { left: 590px; top: 474px; }

  /* Front */
  .facet-field {
    position: absolute; inset: 0;
    background: linear-gradient(135deg, var(--facet-light) 0%, var(--facet-mid) 35%, var(--facet-light) 55%, var(--facet-dark) 80%, var(--facet-light) 100%);
  }
  .front-name {
    position: absolute;
    right: 36px; top: 150px;
    text-align: right;
  }
  .front-name__title {
    display: flex; align-items: center; justify-content: flex-end; gap: 12px;
    font-size: 30px; font-weight: 400; letter-spacing: 2px;
    color: var(--green);
    text-transform: uppercase;
  }
  .front-name__dot {
    width: 16px; height: 16px; border-radius: 50%; background: var(--green);
  }
  .front-name__sub {
    margin-top: 6px;
    font-size: 11px; letter-spacing: 7px; text-transform: uppercase;
    color: var(--muted);
  }

  /* Back */
  .person { position: absolute; left: 0; right: 0; top: 30px; text-align: center; }
  .person__name { font-size: 22px; font-weight: 700; color: var(--green-deep); }
  .person__role { font-size: 10px; margin-top: 4px; color: var(--ink); }
  .brand-mark {
    position: absolute; left: 0; right: 0; top: 98px;
    display: flex; justify-content: center; align-items: center; gap: 8px;
    font-size: 15px; letter-spacing: 1.5px; text-transform: uppercase;
    color: var(--green);
  }
  .brand-mark__dot { width: 10px; height: 10px; border-radius: 50%; background: var(--green); }

  .contacts {
    position: absolute; left: 34px; right: 26px; bottom: 34px;
    display: flex; align-items: flex-end;
  }
  .contacts__col { list-style: none; display: flex; flex-direction: column; gap: 12px; }
  .contacts__col--phones { width: 160px; }
  .contacts__divider {
    width: 1px; height: 120px; margin: 0 18px;
    background: linear-gradient(to bottom, transparent, var(--muted), transparent);
  }
  .contact { display: flex; align-items: center; gap: 10px; font-size: 12px; color: var(--ink); white-space: nowrap; }
  .contact__icon {
    width: 20px; height: 20px; border-radius: 50%; background: var(--green);
    display: flex; align-items: center; justify-content: center; flex: none;
  }
  .contact__icon svg { width: 12px; height: 12px; }
</style>
</head>
<body>

<section class="card card--front" aria-label="Card front">
  <div class="facet-field" role="img" aria-label="Faceted low-poly pattern in soft greys"></div>
  <div class="front-name">
    <div class="front-name__title"><span class="front-name__dot"></span>Halcyon Ridge</div>
    <div class="front-name__sub">Fund</div>
  </div>
</section>

<section class="card card--back" aria-label="Card back">
  <div class="person">
    <h1 class="person__name">Barnaby Whitlock</h1>
    <p class="person__role">Managing Partner</p>
  </div>

  <div class="brand-mark"><span class="brand-mark__dot"></span>Halcyon Ridge</div>

  <div class="contacts">
    <ul class="contacts__col contacts__col--phones">
      <li class="contact">
        <span class="contact__icon"><svg viewBox="0 0 12 12" fill="#fff"><path d="M2 3c0-1 1-1.5 4-1.5S10 2 10 3v1H8V3H4v1H2z M3 5h6l1 5H2z"/></svg></span>
        415.555.0143
      </li>
      <li class="contact">
        <span class="contact__icon"><svg viewBox="0 0 12 12" fill="#fff"><rect x="3" y="1" width="6" height="3"/><rect x="1" y="4" width="10" height="5" rx="1"/><rect x="3" y="7" width="6" height="4" fill="#1a8a3c" stroke="#fff"/></svg></span>
        415.555.0167
      </li>
      <li class="contact">
        <span class="contact__icon"><svg viewBox="0 0 12 12" fill="#fff"><path d="M3 1l2 2-1 1.5c.6 1.4 1.6 2.4 3 3L8.5 6.5l2 2L9 10.5C5 10 2 7 1.5 3z"/></svg></span>
        415.555.0192
      </li>
    </ul>
    <span class="contacts__divider"></span>
    <ul class="contacts__col">
      <li class="contact">
        <span class="contact__icon"><svg viewBox="0 0 12 12" fill="none" stroke="#fff"><rect x="1.5" y="3" width="9" height="6"/><path d="M1.5 3L6 7l4.5-4"/></svg></span>
        barn@halcyonridgefund.example
      </li>
      <li class="contact">
        <span class="contact__icon"><svg viewBox="0 0 12 12" fill="#fff"><path d="M6 1a3.5 3.5 0 0 1 3.5 3.5C9.5 7 6 11 6 11S2.5 7 2.5 4.5A3.5 3.5 0 0 1 6 1z"/><circle cx="6" cy="4.5" r="1.3" fill="#1a8a3c"/></svg></span>
        817 Fern St San Francisco, CA 94111
      </li>
      <li class="contact">
        <span class="contact__icon"><svg viewBox="0 0 12 12" fill="none" stroke="#fff" stroke-width="1.4"><path d="M5 7l2-2"/><path d="M6.5 3.5l1-1a1.8 1.8 0 0 1 2.5 2.5l-1 1"/><path d="M5.5 8.5l-1 1A1.8 1.8 0 0 1 2 7l1-1"/></svg></span>
        www.halcyonridgefund.example
      </li>
    </ul>
  </div>
</section>

</body>
</html>
```